trading data display webpage

We have build a rough wireframe of the two webpages that we want to display .The two wireframes are attached as a pdf document.
there will be login page. after login , the user will see the index page. that is the first page of the wireframe.

what we are displaying is essentially spread data. we are taking the difference in prices are two places and displaying the data. some calculations are done and is shown in the grid.

below the grid we show the behaviour on a graph. we will use bubble chart. I did not find a sample, hence have thrown in a placeholder.

this is time series data ( changes daily) and hence we need to check the behaviour.

the second wire frame shows how the user will choose the source price points and the destination price points.
we are talking here of natural gas prices hence the reference to source prices and destination prices.

you need to design the page/ pages such that the end-user loves it and is easy to use. the intent here is easy to use and easy to understand.
this will be responsive webpage since the end user will check it out on a tablet or a smartphone.

so if possible tell us how the navigation bar, the button bar, etc should fall when the screen size decreases.

I have uploaded 2 files. one is the wireframe ( pdf document) and second is the logo file.

please also let us know where to place the logo.

Target Market(s)

the target market is traders and data analyst

Industry/Entity Type

Build

Colors

Designer to choose colors to be used in the design.

Requirements
Must have
• 1. design for the web.
2. but think how the design will look when the screen size decreases.
3. tell if possible what screen components to keep and what to hide.

```html
<!DOCTYPE html>
<html lang="en">
<head>
<meta charset="utf-8">
<title>Spreadwell – Spread Dashboard</title>
<link rel="stylesheet" href="https://fonts.googleapis.com/css2?family=Maven+Pro:wght@400;500&display=swap">
<style>
  :root {
    --page-bg: #efefef;
    --header-top: #f4f5f7;
    --header-bottom: #e3e5e9;
    --orange: #f26722;
    --green: #8dc63f;
    --navy: #0b4f9c;
    --blue: #1b75bb;
    --sky: #c9dff0;
    --gold: #f7941d;
    --grey-dot: #a7a9ac;
    --line-grey: #b3b3b3;
    --text: #333333;
    --muted: #666666;
    --tab-grey: #d9d9d9;
    --head-dark: #dcdcdc;
    --head-light: #f2f2f2;
    --row-warm: #fde3d9;
    --row-warm-soft: #fdeee8;
    --row-cool: #e0e9f2;
    --row-cool-soft: #e9eff6;
    --panel: #ffffff;
  }
  * { box-sizing: border-box; margin: 0; padding: 0; }
  html, body { width: 1200px; height: 856px; overflow: hidden; }
  body {
    background: var(--page-bg);
    font-family: "Maven Pro", Arial, sans-serif;
    color: var(--text);
    position: relative;
  }
  .site-header {
    position: absolute; left: 0; top: 0; width: 1200px; height: 129px;
    background: linear-gradient(var(--header-top), var(--header-bottom));
    box-shadow: 0 6px 14px rgba(0,0,0,0.12);
  }
  .site-header::after {
    content: ""; position: absolute; left: 0; top: 118px; width: 100%; height: 11px;
    background: linear-gradient(var(--orange) 0 7px, var(--navy) 7px 11px);
  }
  .brand {
    position: absolute; left: 166px; top: 40px;
    display: flex; align-items: center; gap: 10px;
    font-size: 28px; font-weight: 500; color: var(--orange);
  }
  .brand-dot { width: 34px; height: 34px; border-radius: 50%; background: var(--orange); }

  .region-tabs { position: absolute; left: 129px; top: 174px; display: flex; gap: 4px; }
  .region-tab {
    width: 80px; height: 32px; border-radius: 5px 5px 0 0;
    background: var(--tab-grey); color: var(--text);
    font-size: 17px; display: flex; align-items: center; justify-content: center;
  }
  .region-tab.is-active { background: var(--orange); color: #fff; }

  .dashboard {
    position: absolute; left: 118px; top: 206px; width: 964px; height: 543px;
    background: var(--panel); box-shadow: 0 0 8px rgba(0,0,0,0.08);
  }
  .index-picker { position: absolute; top: 22px; }
  .index-picker.source { left: 37px; }
  .index-picker.destination { right: 30px; text-align: right; }
  .picker-label { font-size: 17px; display: flex; align-items: center; gap: 6px; }
  .index-picker.destination .picker-label { justify-content: flex-end; }
  .picker-options { margin-top: 19px; font-size: 17px; color: var(--orange); }
  .picker-options .is-selected { color: var(--green); }
  .picker-options .sep { margin: 0 13px; }

  .spread-table {
    position: absolute; left: 24px; top: 114px; width: 917px;
    border-collapse: collapse; font-size: 17px;
  }
  .spread-table th, .spread-table td { height: 28px; padding: 0 13px; text-align: left; font-weight: 400; }
  .spread-table th { height: 27px; }
  .spread-table th:nth-child(odd) { background: var(--head-dark); }
  .spread-table th:nth-child(even) { background: var(--panel); }
  .spread-table th:nth-child(n+3) { text-align: center; }
  .spread-table th:last-child { text-align: right; }
  .row-warm td { background: var(--row-warm-soft); }
  .row-cool td { background: var(--row-cool-soft); }
  .row-warm td:nth-child(-n+2), .row-warm td:nth-child(3), .row-warm td:nth-child(5), .row-warm td:nth-child(7) { background: var(--row-warm); }
  .row-cool td:nth-child(-n+2), .row-cool td:nth-child(3), .row-cool td:nth-child(5), .row-cool td:nth-child(7) { background: var(--row-cool); }
  .spread-table td:nth-child(1), .spread-table td:nth-child(2) { color: var(--text); }
  .spread-table td:nth-child(1) { width: 135px; }
  .spread-table td:nth-child(2) { width: 115px; }

  .chart { position: absolute; top: 294px; height: 249px; }
  .chart.bubbles { left: 0; width: 483px; }
  .chart.timeline { left: 483px; width: 481px; border-left: 1px solid #d6d6d6; height: 239px; }
  .chart-title { position: absolute; top: 10px; width: 100%; text-align: center; font-size: 15px; }
  .chart.bubbles .chart-title { left: -3px; }
  .chart svg { position: absolute; left: 0; top: 0; }
  .bubble-label { font-family: "Maven Pro", Arial, sans-serif; font-size: 15px; fill: #fff; text-anchor: middle; }

  .site-footer {
    position: absolute; left: 0; top: 779px; width: 1200px; text-align: center;
    font-size: 16px; color: var(--muted); line-height: 20px;
  }
</style>
</head>
<body>
  <header class="site-header">
    <div class="brand"><span class="brand-dot"></span>Spreadwell</div>
  </header>

  <nav class="region-tabs">
    <span class="region-tab is-active">East</span>
    <span class="region-tab">Central</span>
    <span class="region-tab">West</span>
  </nav>

  <main class="dashboard">
    <div class="index-picker source">
      <div class="picker-label">Source Indices
        <svg width="10" height="18" viewBox="0 0 10 18"><path d="M5 1 9 7H1Z M5 17 9 11H1Z" fill="#333"/></svg>
      </div>
      <div class="picker-options"><span class="is-selected">5 days</span><span class="sep">|</span>7 days<span class="sep">|</span>18 days</div>
    </div>
    <div class="index-picker destination">
      <div class="picker-label">Destination Indices
        <svg width="10" height="18" viewBox="0 0 10 18"><path d="M5 1 9 7H1Z M5 17 9 11H1Z" fill="#333"/></svg>
      </div>
      <div class="picker-options"><span class="is-selected">Month</span><span class="sep">|</span>Year</div>
    </div>

    <table class="spread-table">
      <thead>
        <tr><th>Spread-name</th><th>avg sprd</th><th>+ve prob</th><th>-ve prob</th><th>spike prob</th><th>avg supply</th><th>supply cut_prob</th></tr>
      </thead>
      <tbody>
        <tr class="row-warm"><td>Spread1</td><td>item1</td><td></td><td></td><td></td><td></td><td></td></tr>
        <tr class="row-cool"><td>Spread2</td><td>item2</td><td></td><td></td><td></td><td></td><td></td></tr>
        <tr class="row-warm"><td>Spread3</td><td>item3</td><td></td><td></td><td></td><td></td><td></td></tr>
        <tr class="row-cool"><td>Spread4</td><td>item4</td><td></td><td></td><td></td><td></td><td></td></tr>
        <tr class="row-warm"><td>Spread5</td><td>Item5</td><td></td><td></td><td></td><td></td><td></td></tr>
      </tbody>
    </table>

    <section class="chart bubbles">
      <h2 class="chart-title" style="font-weight:400">Spread v/s supply</h2>
      <svg width="483" height="249" viewBox="100 425 411 212">
        <circle cx="178" cy="551" r="31" fill="var(--orange)"/>
        <circle cx="258" cy="511" r="55" fill="var(--green)"/>
        <circle cx="226" cy="590" r="24" fill="var(--sky)"/>
        <circle cx="355" cy="551" r="43" fill="var(--navy)"/>
        <text class="bubble-label" x="178" y="556" style="font-size:13px">12%</text>
        <text class="bubble-label" x="258" y="514" style="font-size:13px">45%</text>
        <text class="bubble-label" x="226" y="595" style="font-size:13px">11%</text>
        <text class="bubble-label" x="355" y="556" style="font-size:13px">32%</text>
      </svg>
    </section>

    <section class="chart timeline">
      <h2 class="chart-title" style="font-weight:400">Spreads across time</h2>
      <svg width="481" height="249" viewBox="511 425 409 212">
        <polyline points="533,455 533,618 893,618" fill="none" stroke="var(--line-grey)" stroke-width="2"/>
        <polyline points="551,580 624,542 685,592 758,499 819,569 883,531" fill="none" stroke="var(--line-grey)" stroke-width="1.6"/>
        <circle cx="624" cy="542" r="9" fill="var(--green)"/>
        <circle cx="685" cy="592" r="9" fill="var(--blue)"/>
        <circle cx="758" cy="499" r="9" fill="var(--gold)"/>
        <circle cx="819" cy="569" r="9" fill="var(--grey-dot)"/>
      </svg>
    </section>
  </main>

  <footer class="site-footer">
    <div>About us | FAQ | Contacts</div>
    <div>Spreadwell 2014</div>
  </footer>
</body>
</html>
```